Flyer Design Project

We need a flyer design for a 1 year old domestic cleaning company based in Wiltshire, England. We provide households with high quality, hard working cleaners. We would like to see designs which use blue (the colour on the logo attatched). The final design should communicate a clean, premier and thorough service in a clear and bold way. We would like the flyer to be A5 with a single sided design. We have attached an A5 word document with the words we would like to be used in the design, what we need is for you to give it some life, colour, artwork and a professional touch. We are perfectionsists which we would like to illustrate to our customer through this flyer.
Updates

payment has been guaranteed!

Sorry..... please no pictures of females on the designs. many thanks

Target Market(s)

females with higher than average income, aged 30-50. Have families and work 9-5.

Industry/Entity Type

It Company

Requirements
Must have
• The flyer must include the logo attatched and the words in the A5 document attatched. With RELIABLE CLEANERS preferably the headline. A5 - single sided.
The Flyer must also include our introductory offer.....
First Clean FREE
Allow us to demonstrate our standards

this should be emphasised.

PLEASE NOTE: can this be added to the list of words on the flyer please:

Ironing service - one day turn around
Nice to have
• some pictures - nothing cheesey. Again, pictures should communicate our modern professional approach.

```html
<!DOCTYPE html>
<html lang="en">
<head>
<meta charset="utf-8">
<title>Brookmere Cleaners – Reliable Cleaners Flyer</title>
<link rel="stylesheet" href="https://fonts.googleapis.com/css2?family=Oswald:wght@300;400&family=Ubuntu:wght@400;500;700&display=swap">
<style>
  :root {
    --deep-blue: #1636d8;
    --mid-blue: #1a78ee;
    --cyan: #1fd0f2;
    --pale-cyan: #9eeefc;
    --white: #ffffff;
    --navy: #0d1b5c;
    --ink: #111111;
    --burst-light: #2aa6f5;
    --burst-dark: #1479e8;
  }
  * { margin: 0; padding: 0; box-sizing: border-box; }
  html, body { width: 1200px; height: 844px; overflow: hidden; background: var(--white); }
  .flyer {
    position: relative;
    width: 1200px;
    height: 844px;
    overflow: hidden;
    font-family: "Ubuntu", sans-serif;
    color: var(--white);
    background: linear-gradient(100deg, var(--deep-blue) 0%, var(--mid-blue) 40%, var(--cyan) 78%, var(--pale-cyan) 100%);
  }
  .backdrop { position: absolute; inset: 0; }

  .brand {
    position: absolute;
    left: 74px;
    top: 26px;
    color: var(--ink);
  }
  .brand-name {
    display: flex;
    align-items: center;
    gap: 10px;
    font-weight: 700;
    font-size: 34px;
    color: var(--navy);
    letter-spacing: -0.5px;
  }
  .brand-mark {
    width: 30px; height: 30px;
    border-radius: 50%;
    background: var(--deep-blue);
  }
  .brand-tagline {
    margin-top: 10px;
    margin-left: 40px;
    font-weight: 700;
    font-size: 15px;
    color: var(--ink);
  }

  .offer-burst {
    position: absolute;
    left: 675px;
    top: 5px;
    width: 390px;
    height: 390px;
    overflow: visible;
  }
  .offer-text {
    position: absolute;
    left: 670px;
    top: 116px;
    width: 400px;
    text-align: center;
    color: var(--white);
  }
  .offer-lead { font-size: 31px; font-weight: 400; line-height: 1; }
  .offer-free { font-size: 72px; font-weight: 700; line-height: 0.95; letter-spacing: 1px; }
  .offer-note { font-size: 20px; line-height: 1.2; margin-top: 6px; }
  .offer-phone { font-size: 21px; margin-top: 18px; }

  .headline {
    position: absolute;
    left: 72px;
    top: 232px;
    font-family: "Oswald", sans-serif;
    font-weight: 300;
    font-size: 52px;
    letter-spacing: 8px;
    color: var(--white);
  }

  .service-list {
    position: absolute;
    left: 180px;
    top: 326px;
    list-style: none;
  }
  .service-list li {
    position: relative;
    padding-left: 28px;
    font-weight: 500;
    font-size: 27px;
    line-height: 54px;
  }
  .service-list li::before {
    content: "";
    position: absolute;
    left: 0; top: 22px;
    width: 13px; height: 13px;
    border-radius: 50%;
    background: var(--white);
  }

  .contact-email {
    position: absolute;
    left: 186px;
    top: 738px;
    font-size: 16px;
    font-weight: 500;
  }

  .photo { position: absolute; }
  .photo-spray {
    left: 0; top: 410px; width: 150px; height: 390px;
    border-radius: 0 40px 40px 0;
    background: linear-gradient(180deg, #f2df3a 0%, #e6c820 30%, #bfe7f5 55%, #8fd3ee 100%);
  }
  .photo-caddy {
    left: 540px; top: 400px; width: 140px; height: 140px;
    border-radius: 18px;
    background: linear-gradient(160deg, #e8eef2 0%, #c3d2dc 55%, #f0d84a 100%);
  }
  .photo-bucket {
    left: 750px; top: 540px; width: 130px; height: 150px;
    border-radius: 20px 20px 40px 40px;
    background: linear-gradient(170deg, #f28bb0 0%, #8fc8f2 40%, #f4e06a 100%);
  }
  .photo-sponges {
    left: 990px; top: 510px; width: 210px; height: 334px;
    border-radius: 40px 0 0 0;
    background: linear-gradient(160deg, #4bc95a 0%, #8a5ee0 35%, #5a7ff0 55%, #ff8a3c 80%, #f26a8a 100%);
  }
</style>
</head>
<body>
<main class="flyer">
  <svg class="backdrop" width="1200" height="844" viewBox="0 0 1200 844" aria-hidden="true">
    <polygon points="0,0 1200,0 1200,40 0,190" fill="#ffffff"/>
    <polygon points="1200,420 1200,844 760,844" fill="#bff4fd" opacity="0.45"/>
  </svg>

  <header class="brand">
    <div class="brand-name"><span class="brand-mark"></span>Brookmere Cleaners</div>
    <div class="brand-tagline">Premier Domestic Cleaners</div>
  </header>

  <svg class="offer-burst" viewBox="-195 -195 390 390" aria-hidden="true">
    <defs>
      <radialGradient id="burstFill" gradientUnits="userSpaceOnUse" cx="0" cy="0" r="195">
        <stop offset="0%" stop-color="#2aa6f5"/>
        <stop offset="100%" stop-color="#1479e8"/>
      </radialGradient>
      <polygon id="burstPoint" points="0,-188 162.8,94 -162.8,94"/>
    </defs>
    <g class="burst-outline" fill="#ffffff" stroke="#ffffff" stroke-width="8" stroke-linejoin="miter">
      <use href="#burstPoint" transform="rotate(0)"/>
      <use href="#burstPoint" transform="rotate(8)"/>
      <use href="#burstPoint" transform="rotate(16)"/>
      <use href="#burstPoint" transform="rotate(24)"/>
      <use href="#burstPoint" transform="rotate(32)"/>
      <use href="#burstPoint" transform="rotate(40)"/>
      <use href="#burstPoint" transform="rotate(48)"/>
      <use href="#burstPoint" transform="rotate(56)"/>
      <use href="#burstPoint" transform="rotate(64)"/>
      <use href="#burstPoint" transform="rotate(72)"/>
      <use href="#burstPoint" transform="rotate(80)"/>
      <use href="#burstPoint" transform="rotate(88)"/>
      <use href="#burstPoint" transform="rotate(96)"/>
      <use href="#burstPoint" transform="rotate(104)"/>
      <use href="#burstPoint" transform="rotate(112)"/>
    </g>
    <g class="burst-fill" fill="url(#burstFill)">
      <use href="#burstPoint" transform="rotate(0)"/>
      <use href="#burstPoint" transform="rotate(8)"/>
      <use href="#burstPoint" transform="rotate(16)"/>
      <use href="#burstPoint" transform="rotate(24)"/>
      <use href="#burstPoint" transform="rotate(32)"/>
      <use href="#burstPoint" transform="rotate(40)"/>
      <use href="#burstPoint" transform="rotate(48)"/>
      <use href="#burstPoint" transform="rotate(56)"/>
      <use href="#burstPoint" transform="rotate(64)"/>
      <use href="#burstPoint" transform="rotate(72)"/>
      <use href="#burstPoint" transform="rotate(80)"/>
      <use href="#burstPoint" transform="rotate(88)"/>
      <use href="#burstPoint" transform="rotate(96)"/>
      <use href="#burstPoint" transform="rotate(104)"/>
      <use href="#burstPoint" transform="rotate(112)"/>
    </g>
  </svg>
  <section class="offer-text">
    <div class="offer-lead">First Clean</div>
    <div class="offer-free">FREE</div>
    <div class="offer-note">Allow us to demonstrate<br>our standards...</div>
    <div class="offer-phone">Tele: 07700 900418</div>
  </section>

  <h1 class="headline">RELIABLE CLEANERS!</h1>

  <ul class="service-list">
    <li>Personalised Service</li>
    <li>Constantly Thorough</li>
    <li>Hassel Free</li>
    <li>Insured</li>
    <li>Regular Weekly Cleans</li>
    <li>No Contracts</li>
    <li>Ironing Service - One day turn around</li>
  </ul>

  <p class="contact-email">Email: brookmerecleaners@example.co.uk</p>

  <div class="photo photo-spray" role="img" aria-label="Photo of a gloved hand holding a spray bottle"></div>
  <div class="photo photo-caddy" role="img" aria-label="Photo of a cleaning caddy with gloves and brushes"></div>
  <div class="photo photo-bucket" role="img" aria-label="Photo of a bucket filled with cleaning supplies"></div>
  <div class="photo photo-sponges" role="img" aria-label="Photo of a stack of colourful sponges"></div>
</main>
</body>
</html>
```